Cloud Based Internet Protection Service Business Cards

I would like a professionally designed business card. I already have a logo which I have attached.

The business is an online cloud based internet protection service aimed parents, particularly at non-technical parents and also schools.

The card should be be quite simple in its design, not to full of text and give its information in a clear and concise manner

Target Market(s)

Parents (especially non-technical parents) and also schools

Industry/Entity Type

Internet

Colors

Designer to choose colors to be used in the design.

Requirements
Should not have
• Too much text or be too cluttered. No decorative fonts, just a clear and concise font.

```html
<!DOCTYPE html>
<html lang="en">
<head>
<meta charset="utf-8">
<title>Harbor Shield Business Card</title>
<link href="https://fonts.googleapis.com/css2?family=Open+Sans:wght@400;600;700&display=swap" rel="stylesheet">
<style>
  :root {
    --page-bg: #e9eaeb;
    --card-bg: #1e1b1a;
    --brand-silver: #d9d9d9;
    --brand-blue: #2b8fd4;
    --text-light: #e6e6e6;
    --divider: #3a3634;
    --card-shadow: rgba(0, 0, 0, 0.22);
  }
  * { box-sizing: border-box; margin: 0; padding: 0; }
  html, body {
    width: 1200px; height: 675px; overflow: hidden;
    background: var(--page-bg);
    font-family: "Open Sans", Arial, sans-serif;
  }
  .canvas {
    position: relative; width: 1200px; height: 675px;
    display: flex; align-items: center; justify-content: center; gap: 60px;
  }
  .card {
    position: relative; width: 525px; height: 300px;
    background: var(--card-bg);
    box-shadow: 0 10px 24px var(--card-shadow);
    overflow: hidden;
  }
  .brand {
    display: flex; align-items: center; gap: 12px;
    color: var(--brand-silver);
    font-weight: 700; letter-spacing: 2px;
  }
  .brand-dot {
    width: 18px; height: 18px; border-radius: 50%;
    background: var(--brand-blue); flex: none;
  }
  .card-front .brand {
    position: absolute; left: 70px; top: 50%; transform: translateY(-50%);
    font-size: 34px;
  }
  .card-back .brand {
    position: absolute; left: 34px; top: 50%; transform: translateY(-50%);
    font-size: 21px; letter-spacing: 1.5px;
  }
  .card-back .brand-dot { width: 14px; height: 14px; }
  .divider {
    position: absolute; left: 262px; top: 70px; width: 1px; height: 170px;
    background: var(--divider);
  }
  .contact {
    position: absolute; left: 285px; top: 88px;
    color: var(--text-light); font-size: 12.5px; line-height: 1.45;
  }
  .contact-name { color: var(--brand-blue); font-weight: 700; font-size: 14px; }
  .contact-title { font-size: 11px; margin-bottom: 12px; }
  .contact-row { display: flex; align-items: center; gap: 6px; }
  .contact-row svg { width: 11px; height: 11px; fill: var(--brand-blue); flex: none; }
  .gap { width: 6px; }
  .highlight { color: var(--brand-blue); }
</style>
</head>
<body>
<main class="canvas">
  <section class="card card-front">
    <div class="brand"><span class="brand-dot"></span>HARBOR SHIELD</div>
  </section>

  <section class="card card-back">
    <div class="brand"><span class="brand-dot"></span>HARBOR SHIELD</div>
    <div class="divider"></div>
    <div class="contact">
      <p class="contact-name">Your Long Name</p>
      <p class="contact-title">Your Title</p>
      <p class="contact-row">
        <svg viewBox="0 0 12 12"><path d="M6 0a4 4 0 0 0-4 4c0 3 4 8 4 8s4-5 4-8a4 4 0 0 0-4-4zm0 5.5A1.5 1.5 0 1 1 6 2.5a1.5 1.5 0 0 1 0 3z"/></svg>
        Your office or home address
      </p>
      <p class="contact-row">
        <svg viewBox="0 0 12 12"><path d="M1 4c0-2 1-3 3-3h4c2 0 3 1 3 3l-3 .5L7.5 3h-3L4 4.5zM2 6h8l1 5H1z"/></svg>
        000-000-0000<span class="gap"></span>
        <svg viewBox="0 0 12 12"><path d="M3 0h6v12H3zm1 1v8h4V1z"/></svg>
        0000000000
      </p>
      <p class="contact-row">
        <svg viewBox="0 0 12 12"><path d="M0 2h12v8H0zm1 1 5 4 5-4z"/></svg>
        yourname@yourwebsite.com
      </p>
      <p class="contact-row">
        <svg viewBox="0 0 12 12"><path d="M6 0a6 6 0 1 0 0 12A6 6 0 0 0 6 0zm-.6 1.2v2.2H3.5c.4-1 1.1-1.8 1.9-2.2zm1.2 0c.8.4 1.5 1.2 1.9 2.2H6.6zM1.4 4.6h4v2.8h-4a4.8 4.8 0 0 1 0-2.8zm5.2 0h4a4.8 4.8 0 0 1 0 2.8h-4zM3.5 8.6h1.9v2.2c-.8-.4-1.5-1.2-1.9-2.2zm3.1 0h1.9c-.4 1-1.1 1.8-1.9 2.2z"/></svg>
        www.<span class="highlight">yourwebsite</span>.com
      </p>
    </div>
  </section>
</main>
</body>
</html>
```